Business Card Design for The Lending Nook Inc.

We need a business card design for our mortgage company: "The Lending Nook Inc."

Need to have Social Media Account on there as a possibility

Industry/Entity Type

Business

```html
<!DOCTYPE html>
<html lang="en">
<head>
<meta charset="utf-8">
<title>The Lending Nook Inc. – Business Cards</title>
<link href="https://fonts.googleapis.com/css2?family=Arimo:wght@400;500&display=swap" rel="stylesheet">
<style>
  :root {
    --brand-blue: #1f5aa6;
    --ink: #3d3d3f;
    --card: #ffffff;
    --backdrop: #ececec;
    --edge: #d6d6d6;
  }
  html, body {
    margin: 0;
    padding: 0;
    width: 1200px;
    height: 799px;
    overflow: hidden;
    background: var(--backdrop);
    font-family: "Arimo", Arial, sans-serif;
  }
  .canvas {
    position: relative;
    width: 1200px;
    height: 799px;
  }
  .card {
    position: absolute;
    background: var(--card);
    border: 1px solid var(--edge);
    box-sizing: border-box;
  }
  /* Front */
  .card--front {
    left: 50px;
    top: 52px;
    width: 606px;
    height: 346px;
  }
  .front-mark {
    position: absolute;
    left: 88px;
    top: 148px;
    width: 50px;
    height: 50px;
    border: 4px solid var(--brand-blue);
    border-radius: 50%;
    box-sizing: border-box;
  }
  .front-name {
    position: absolute;
    left: 156px;
    top: 148px;
    line-height: 50px;
    font-size: 40px;
    font-weight: 500;
    color: var(--brand-blue);
    white-space: nowrap;
    letter-spacing: -0.3px;
  }
  /* Back */
  .card--back {
    left: 535px;
    top: 282px;
    width: 605px;
    height: 347px;
  }
  .back-mark {
    position: absolute;
    left: 40px;
    top: 140px;
    width: 190px;
    text-align: center;
  }
  .back-mark__dot {
    display: block;
    width: 22px;
    height: 22px;
    margin: 0 auto 10px;
    border-radius: 50%;
    background: var(--brand-blue);
  }
  .back-mark__name {
    font-size: 24px;
    line-height: 28px;
    font-weight: 500;
    color: var(--brand-blue);
  }
  .divider {
    position: absolute;
    left: 267px;
    top: 42px;
    width: 2px;
    height: 266px;
    background: var(--ink);
  }
  .details {
    position: absolute;
    left: 311px;
    top: 68px;
    color: var(--ink);
  }
  .details__name {
    margin: 0;
    font-size: 32px;
    line-height: 38px;
    font-weight: 400;
  }
  .details__role {
    margin: 0 0 18px;
    font-size: 16px;
    line-height: 20px;
    color: var(--brand-blue);
  }
  .contact {
    list-style: none;
    margin: 0;
    padding: 0;
    font-size: 15.5px;
    line-height: 24.5px;
  }
  .contact__label {
    color: var(--brand-blue);
  }
  .social {
    position: absolute;
    left: 311px;
    top: 252px;
    display: flex;
    align-items: flex-end;
    gap: 10px;
    color: var(--ink);
    font-size: 16px;
  }
  .social__icon {
    width: 27px;
    height: 27px;
    background: #3b5a9a;
  }
  .social__handle {
    line-height: 18px;
    margin-bottom: -2px;
  }
</style>
</head>
<body>
<main class="canvas">
  <section class="card card--front" aria-label="Card front">
    <span class="front-mark" aria-hidden="true"></span>
    <span class="front-name">The Lending Nook Inc.</span>
  </section>

  <section class="card card--back" aria-label="Card back">
    <div class="back-mark">
      <span class="back-mark__dot" aria-hidden="true"></span>
      <span class="back-mark__name">The Lending Nook</span>
    </div>
    <div class="divider" aria-hidden="true"></div>
    <div class="details">
      <h1 class="details__name">Alex Carter</h1>
      <p class="details__role">Mortgage Advisor</p>
      <ul class="contact">
        <li><span class="contact__label">t:</span> 555 (010) 4821</li>
        <li><span class="contact__label">e:</span> hello@lendingnook.com</li>
        <li><span class="contact__label">w:</span> www.lendingnook.com</li>
      </ul>
    </div>
    <div class="social">
      <span class="social__icon" aria-hidden="true"></span>
      <span class="social__handle">The Lending Nook</span>
    </div>
  </section>
</main>
</body>
</html>
```